Very Simple Web Redesign Project - Using Photoshop

Required is a very simple website home page redesign for the following site: http://www.kestrelslateworks.com.au/
I require this as a Photoshop design.
The basic look and feel of the site needs to remain.
Specifically the colours don't need to be changed.
The positioning of the site is currently correct for the target market.
The site does not need to be made super slick looking. Just upgraded to a new version.
The current text can all be used.
The only menus necessary are a horizontal menu at the top, and a simple horizontal text menu at the bottom of the page. Do NOT retain the vertical menu on the home page (having the items "Our Gallery", "Our Services", "Enquire Now").
Give the horizontal menu the following items:
Home | Slate Roof Repairs | Slate Reroofing | Slate Roof Benefits | Other Services | Photo Gallery | FAQ's | Free Quote | Contact Us
The picture of the house at the top RHS of the page needs to be reduced in size by approx 50% and moved to the top LHS of the page.
Please place the following text into the top of the page:
"Call Now: 0427 618 302"
Keep the four pictures on the home page layout. Some larger images attached.
Thanks,
Ned
Updates
Hi,
Thanks for all the designs.
I am working with my client to get which one they like the most.
Thanks,
Ned

```html
<!DOCTYPE html>
<html lang="en">
<head>
<meta charset="utf-8">
<title>Kestrel Slateworks – The Slate Roof Specialists</title>
<link rel="stylesheet" href="https://fonts.googleapis.com/css2?family=Arimo:wght@400;700&family=Gelasio:wght@400;700&display=swap">
<style>
  :root {
    --green-dark: #2f7a14;
    --green: #3f8f1c;
    --green-light: #6cbf2e;
    --green-text: #4f9e1c;
    --lime: #8fd12a;
    --white: #ffffff;
    --ink: #222222;
    --grey-text: #5f5f5f;
    --grey-head: #5a5a5a;
    --panel: #f5f6f4;
    --frame: #cfd0cd;
    --night: #161616;
    --rule: #d9d9d9;
  }
  * { margin: 0; padding: 0; box-sizing: border-box; }
  html, body { width: 1152px; height: 1200px; overflow: hidden; }
  body {
    position: relative;
    background: var(--night);
    font-family: "Gelasio", Georgia, serif;
    color: var(--grey-text);
  }

  /* Header */
  .site-header {
    position: absolute; left: 0; top: 0; width: 1152px; height: 215px;
    border-top: 4px solid var(--white);
    background: linear-gradient(180deg, var(--green-dark) 0%, var(--green) 70%, #3a8a19 100%);
    overflow: hidden;
  }
  .site-header svg.swoosh { position: absolute; left: 0; top: 0; }
  .brand {
    position: absolute; left: 64px; top: 60px;
    display: flex; align-items: center; gap: 18px;
  }
  .brand-mark { width: 78px; height: 78px; background: #5b7d3c; }
  .brand-name {
    font-family: "Gelasio", Georgia, serif;
    font-size: 45px; color: var(--white); font-weight: 400;
  }
  .header-phone {
    position: absolute; right: 52px; top: 118px;
    display: flex; align-items: center; gap: 10px;
    font-family: "Arimo", Arial, sans-serif; font-weight: 700;
    font-size: 26px; color: var(--white);
  }
  .phone-icon {
    width: 24px; height: 24px; border-radius: 4px; background: var(--lime);
    display: flex; align-items: center; justify-content: center;
  }

  /* Main navigation */
  .main-nav {
    position: absolute; left: 0; top: 215px; width: 1152px; height: 50px;
    background: linear-gradient(180deg, #ffffff 0%, #f1f1f1 60%, #e2e2e2 100%);
    display: flex; align-items: center; padding-left: 60px;
    font-family: "Arimo", Arial, sans-serif; font-size: 14px; color: var(--ink);
  }
  .main-nav a { color: var(--ink); text-decoration: none; }
  .main-nav a.current { color: var(--green-text); }
  .main-nav .sep { margin: 0 13px; }

  /* Content panel */
  .content {
    position: absolute; left: 54px; top: 275px; width: 1046px; height: 797px;
    background: var(--panel);
  }
  .gallery {
    position: absolute; left: 8px; top: 10px; width: 1032px; height: 385px;
    background: var(--frame); border-radius: 3px;
  }
  .photo { position: absolute; border: 3px solid var(--white); }
  .photo-a { left: 8px; top: 10px; width: 278px; height: 361px;
    background: linear-gradient(180deg, #b9c7d4 0%, #6c6f74 35%, #4f5257 70%, #8a8a86 100%); }
  .photo-b { left: 296px; top: 10px; width: 274px; height: 361px;
    background: linear-gradient(160deg, #c9b8a7 0%, #7d7670 40%, #6a6560 70%, #8a5c44 100%); }
  .photo-c { left: 580px; top: 10px; width: 441px; height: 173px;
    background: linear-gradient(120deg, #757c86 0%, #4e535c 50%, #5a5f66 80%, #8b7b6b 100%); }
  .photo-d { left: 580px; top: 193px; width: 441px; height: 178px;
    background: linear-gradient(120deg, #5c6066 0%, #73777c 40%, #d9cfa9 75%, #8d7d70 100%); }

  .intro { position: absolute; left: 20px; top: 430px; width: 700px; }
  .intro h1 {
    font-family: "Arimo", Arial, sans-serif; font-weight: 700;
    font-size: 21px; color: var(--grey-head); margin-bottom: 20px; letter-spacing: 0.2px;
  }
  .intro h1 span { color: var(--green-text); }
  .intro p { font-size: 14.5px; line-height: 19.5px; margin-bottom: 19px; }
  .intro a { color: #2a2ad0; text-decoration: underline; }

  .quote-box {
    position: absolute; left: 740px; top: 430px; width: 282px; height: 273px;
    background: linear-gradient(180deg, #ffffff 0%, #f4f4f4 100%);
    border: 1px solid var(--rule); box-shadow: 0 1px 4px rgba(0,0,0,0.18);
  }
  .quote-head {
    margin: 6px; height: 40px;
    background: linear-gradient(180deg, var(--lime) 0%, #69b31d 100%);
    display: flex; align-items: center; justify-content: space-between; padding: 0 8px;
    font-family: "Arimo", Arial, sans-serif; font-weight: 700; font-size: 18px; color: var(--white);
  }
  .quote-head strong { color: #173d05; }
  .quote-head .badge { width: 30px; height: 30px; background: #2d4a21; border-radius: 4px; }
  .quote-box p { padding: 8px 14px 0; font-size: 14.5px; line-height: 19.5px; }
  .quote-box hr { border: 0; border-top: 1px solid var(--rule); margin: 30px 8px 0; }
  .quote-phone {
    padding: 18px 16px; font-family: "Arimo", Arial, sans-serif; font-weight: 700;
    font-size: 20px; color: var(--grey-head);
  }
  .quote-phone span { color: var(--green-text); margin-left: 8px; letter-spacing: 1.5px; }

  /* Footer */
  .site-footer {
    position: absolute; left: 0; top: 1090px; width: 1152px; height: 110px;
    border-top: 3px solid var(--white);
    background: linear-gradient(180deg, var(--green-dark) 0%, var(--green) 100%);
    color: var(--white);
  }
  .footer-nav {
    position: absolute; left: 52px; top: 31px;
    font-family: "Arimo", Arial, sans-serif; font-size: 11px;
  }
  .footer-nav a { color: var(--white); text-decoration: none; }
  .footer-nav a.current { text-decoration: underline; }
  .footer-nav .sep { margin: 0 8px; }
  .copyright { position: absolute; left: 52px; top: 50px; font-family: "Arimo", Arial, sans-serif; font-size: 11px; }
  .legal {
    position: absolute; left: 938px; top: 28px;
    font-family: "Gelasio", Georgia, serif; font-weight: 700; font-size: 15px; line-height: 20px;
  }
</style>
</head>
<body>

<header class="site-header">
  <svg class="swoosh" width="1152" height="215" viewBox="0 0 1152 215" aria-hidden="true">
    <path d="M0 0 H1152 V40 C900 10 600 40 300 60 C180 68 80 60 0 50 Z" fill="#2a6e10" opacity="0.6"/>
    <path d="M140 60 C400 40 700 80 1152 150 V110 C800 60 450 30 140 60 Z" fill="#7cc43a" opacity="0.45"/>
  </svg>
  <div class="brand">
    <div class="brand-mark"></div>
    <div class="brand-name">Kestrel Slateworks</div>
  </div>
  <div class="header-phone">
    <span class="phone-icon">
      <svg width="14" height="14" viewBox="0 0 24 24" aria-hidden="true"><path fill="#ffffff" d="M6.6 10.8a15.1 15.1 0 0 0 6.6 6.6l2.2-2.2c.3-.3.7-.4 1-.2 1.1.4 2.3.6 3.6.6.6 0 1 .4 1 1V20c0 .6-.4 1-1 1A17 17 0 0 1 3 4c0-.6.4-1 1-1h3.5c.6 0 1 .4 1 1 0 1.3.2 2.5.6 3.6.1.3 0 .7-.2 1z"/></svg>
    </span>
    0427 618 302
  </div>
</header>

<nav class="main-nav">
  <a class="current" href="#">Home</a><span class="sep">|</span>
  <a href="#">Slate Roof Repairs</a><span class="sep">|</span>
  <a href="#">Slate Reroofing</a><span class="sep">|</span>
  <a href="#">Slate Roof Benefits</a><span class="sep">|</span>
  <a href="#">Other Services</a><span class="sep">|</span>
  <a href="#">Photo Gallery</a><span class="sep">|</span>
  <a href="#">FAQ's</a><span class="sep">|</span>
  <a href="#">Free Quote</a><span class="sep">|</span>
  <a href="#">Contact Us</a>
</nav>

<main class="content">
  <section class="gallery">
    <div class="photo photo-a" role="img" aria-label="Photo of a repaired grey slate roof above a bay window"></div>
    <div class="photo photo-b" role="img" aria-label="Photo of a slate roof beside a brick wall and balcony railing"></div>
    <div class="photo photo-c" role="img" aria-label="Photo of a slate roof with a small dormer window"></div>
    <div class="photo photo-d" role="img" aria-label="Photo of new slate roofing around a green-framed window"></div>
  </section>

  <section class="intro">
    <h1>KESTREL SLATEWORKS - <span>THE SLATE ROOF SPECIALISTS</span></h1>
    <p>At Kestrel Slateworks we specialize in the upkeep, maintenance, repair and replacement of all types of slate roof as well as wood shingles. &nbsp;We can track down the leak that just won't go away or give your house a complete re-roof. We can also provide all your guttering needs.</p>
    <p>Kestrel Slateworks is a small company and as such we do not have the overheads that larger companies do. Quality work and attention to detail are our trademark.</p>
    <p>All photos on this website consist of work which I have personally done. &nbsp;The above photos provide at a quick glance a reasonable cross section of the type of work I do.</p>
    <p>By clicking on the Photo Gallery link you can see other work including some before and after shots.</p>
    <p>Feel free to call at your earliest convenience to organise an obligation free quote or fill out a form by clicking on the <a href="#">Contact Us</a> link below.</p>
  </section>

  <aside class="quote-box">
    <div class="quote-head"><div>CALL FOR <strong>FREE QUOTE</strong></div><div class="badge"></div></div>
    <p>We service all inner city suburbs of Sydney roughly covering an area encompassing Gordon to Epping, Mosman to Bondi, Coogee to Kogarah and Kingsgrove to Burwood and Concord</p>
    <hr>
    <div class="quote-phone">Phone : <span>0427 618 302</span></div>
  </aside>
</main>

<footer class="site-footer">
  <nav class="footer-nav">
    <a class="current" href="#">Home</a><span class="sep">|</span>
    <a href="#">Slate Roof Repairs</a><span class="sep">|</span>
    <a href="#">Slate Reroofing</a><span class="sep">|</span>
    <a href="#">Slate Roof Benefits</a><span class="sep">|</span>
    <a href="#">Other Services</a><span class="sep">|</span>
    <a href="#">Photo Gallery</a><span class="sep">|</span>
    <a href="#">FAQ's</a><span class="sep">|</span>
    <a href="#">Free Quote</a><span class="sep">|</span>
    <a href="#">Contact Us</a>
  </nav>
  <div class="copyright">© All Rights Reserved</div>
  <div class="legal">Abn 47 309 816 225<br>Lic No. 204718B</div>
</footer>

</body>
</html>
```